Summit Vitality Nutrition Booklet

Task Description

**Project Title**: Summit Vitality Nutrition Introductory Document Design

**Description**:
We need a comprehensive and visually appealing introductory document for Summit Vitality, a specialized gym based in Victoria, British Columbia. Our gym focuses on personal training, habit changing, and nutrition coaching, with a special emphasis on longevity. This document will be used to introduce new clients to our nutrition programming, providing them with all necessary information, tips, and guidance to support their health and wellness journey.

**Business Background**:
Summit Vitality is dedicated to helping clients achieve their health and fitness goals through personalized training and nutrition plans. All our coaches hold degrees in sports science and are committed to promoting long-term health and longevity. We offer various services, including screenings, comprehensive testing, nutrition coaching, and assessments of sleep hygiene and stress levels. Our goal is to empower clients to make educated choices for their health and to provide them with the tools they need to succeed.

**Document Requirements**:
1. **Cover Page**:
- Title: "Summit Vitality Nutrition Introductory Guide"
- Subtitle: "Your Comprehensive Guide to Nutrition and Longevity"
- Include Summit Vitality logo and branding elements
- Visually engaging design that reflects health, wellness, and longevity

2. **Table of Contents**:
- Organized and easy to navigate sections

3. **Introduction**:
- Brief overview of Summit Vitality and our nutrition philosophy
- Emphasis on personalized coaching and habit changing

4. **Nutrition Programming Overview**:
- Detailed description of our nutrition coaching services
- Information on how we integrate nutrition with personal training for optimal results
- Explanation of the role of nutrition in longevity and overall health

5. **Meal Prep Tips and Tricks**:
- Practical advice for meal planning and preparation
- Tips for maintaining a balanced and nutritious diet
- Easy-to-follow guidelines and examples

6. **Sample Meal Plans**:
- Examples of balanced meal plans tailored to different fitness goals
- Nutritional breakdown and portion sizes

7. **Holistic Nutrition and Longevity**:
- Overview of the importance of holistic nutrition in promoting longevity
- Key nutrients and foods that support long-term health

8. **Client Testimonials**:
- Real-life success stories from clients who have benefited from our nutrition coaching

9. **Contact Information**:
- How to reach our nutrition coaches for further guidance and support
- Summit Vitality contact details (phone number: 250-764-2018, email: info@summitvitality.example)

**Design Preferences**:
- Use a clean, modern, and professional design style
- Incorporate our brand colors (please refer to our logo and branding guidelines)
- Use high-quality images that convey health, wellness, and vitality
- Ensure the document is easy to read with clear headings and subheadings

**Final Deliverables**:
- High-resolution PDF of the complete document
- Source files (e.g., Adobe InDesign or Illustrator) for future edits

We are looking for a design that not only informs but also inspires our clients to take control of their nutrition and health. All of the text is already written with the fonts that we are hoping to use. I will upload it below along with an example of one that I really like from one of our competitors Thank you!

Target Market(s)

### Target Market for Summit Vitality Nutrition Program **Primary Target Market**: 1. **Age Group**: - Adults aged 35-65 years old 2. **Gender**: - Both males and females 3. **Location**: - Residents of Victoria, British Columbia, and surrounding areas 4. **Demographics**: - Middle to upper-middle class income - Professionals and business owners - Parents, especially those looking to improve family health 5. **Psychographics**: - Health-conscious individuals seeking to improve their overall wellness - People interested in longevity and preventive health - Those who value personalized coaching and tailored fitness plans - Individuals motivated by evidence-based health strategies and scientific approaches 6. **Lifestyle**: - Busy professionals who need efficient and effective nutrition solutions - Active individuals who are already engaged in regular physical activity - People who have tried traditional gyms or diet plans without achieving long-term success - Individuals interested in holistic approaches to health, including nutrition, sleep, and stress management **Secondary Target Market**: 1. **Age Group**: - Young adults aged 25-34 years old 2. **Demographics**: - Young professionals and early-career individuals - Health and fitness enthusiasts 3. **Psychographics**: - Individuals seeking to establish healthy habits early in life - People interested in building a foundation for long-term health and wellness - Those who appreciate innovative and science-based approaches to fitness and nutrition 4. **Lifestyle**: - Tech-savvy individuals who use apps and digital tools for health management - People who participate in community events, such as fitness classes, marathons, and health seminars - Individuals looking for a supportive community and personalized guidance to achieve their health goals **Key Motivations and Pain Points**: 1. **Motivations**: - Desire to improve overall health and wellness - Interest in increasing longevity and quality of life - Seeking personalized and effective nutrition and fitness plans - Need for accountability and expert guidance - Aspiration to maintain a healthy weight and improve physical fitness 2. **Pain Points**: - Frustration with generic diet plans that do not yield results - Difficulty finding reliable and personalized nutrition advice - Struggles with maintaining consistency and motivation - Limited time for meal preparation and planning - Concerns about aging and maintaining health as they get older **Marketing Channels**: - Social media platforms (Instagram, Facebook, LinkedIn) to reach health-conscious individuals and professionals - Email marketing to provide valuable content and updates to our existing and potential clients - Community events and seminars to engage with local residents and promote our services - Collaboration with local health and wellness influencers to expand our reach By understanding and addressing the needs and preferences of our target market, Summit Vitality can effectively tailor our nutrition program to provide maximum value and support to our clients.

Industry/Entity Type

Health and wellness

Font styles to use
Other font styles liked:
• Fonts are in the document I attached

Requirements
Must have
• ### Project Must-Haves for Summit Vitality Nutrition Introductory Document 1. **Professional Design**: - Clean, modern, and professional design style that aligns with Summit Vitality branding. - Use of high-quality images that convey health, wellness, and vitality. - Consistent use of brand colors, fonts, and logos as per our branding guidelines. 2. **Comprehensive Content**: - Detailed overview of Summit Vitality and its nutrition philosophy. - Clear and engaging introduction to the nutrition program. - Practical meal prep tips and tricks tailored to our clients' needs. - Sample meal plans with nutritional breakdown and portion sizes. - Information on holistic nutrition and its role in promoting longevity. 3. **Client-Centric Approach**: - Easy-to-follow guidelines and actionable advice. - Inclusion of client testimonials to build trust and credibility. - Emphasis on personalized coaching and habit-changing strategies. 4. **Clear Structure and Navigation**: - Organized table of contents for easy navigation. - Clear headings, subheadings, and sections to make the document easy to read. - Logical flow of information from introduction to detailed sections. 5. **Contact and Support Information**: - Prominent display of Summit Vitality contact details (phone number, email, and website). - Information on how clients can reach our nutrition coaches for further guidance and support. 6. **High-Quality Deliverables**: - High-resolution PDF of the complete document. - Source files (e.g., Adobe InDesign or Illustrator) for future edits and updates. 7. **Engaging Visual Elements**: - Use of infographics and visual aids to simplify complex information. - Inclusion of charts or graphs to illustrate key points and data. 8. **Client Accessibility**: - Ensure the document is accessible and easy to understand for clients with varying levels of nutritional knowledge. - Provide links to additional resources or further reading for interested clients. 9. **Call to Action**: - Clear calls to action throughout the document, encouraging clients to reach out for personalized coaching, book consultations, or engage with additional services. 10. **Review and Feedback**: - Opportunity for review and feedback on draft designs to ensure the final product meets our expectations. - Incorporate any necessary revisions based on feedback to achieve the desired outcome. By including these must-haves, we can ensure the Summit Vitality Nutrition Introductory Document is both informative and visually appealing, providing valuable support to our clients and enhancing their experience with our nutrition program. ### Summit Vitality Brand Colors #### Primary Colors - **Navy Blue**: `#001F3F` ![#001F3F](https://via.placeholder.com/50/001F3F/FFFFFF?text=+) - **Muted Earthy Blue**: `#3A5F70` ![#3A5F70](https://via.placeholder.com/50/3A5F70/FFFFFF?text=+) #### Secondary Colors - **White**: `#FFFFFF` ![#FFFFFF](https://via.placeholder.com/50/FFFFFF/000000?text=+) - **Gray**: `#A0A0A0` ![#A0A0A0](https://via.placeholder.com/50/A0A0A0/FFFFFF?text=+) #### Accent Color - **Darker Moss Green**: `#556B2F` ![#556B2F](https://via.placeholder.com/50/556B2F/FFFFFF?text=+) These colors should provide a cohesive, earthy, and professional palette that aligns with the West Coast aesthetic and the branding of Summit Vitality.
Nice to have
• ### Nice-to-Haves for Summit Vitality Nutrition Introductory Document 1. **Interactive Elements**: - Incorporate clickable links to recipes, additional resources, or external articles for more in-depth information. - Interactive PDFs with embedded videos explaining meal prep techniques or demonstrating exercises. 2. **Personalized Sections**: - Space for clients to fill in their personal goals, dietary preferences, and notes. - Customizable meal plans that clients can adjust according to their preferences and needs. 3. **Digital Integration**: - QR codes linking to online resources, such as instructional videos, recipe blogs, or workout plans. - Integration with our gym’s app or website for easy access to additional content and tools. 4. **Success Stories and Case Studies**: - Detailed case studies of clients who have successfully improved their health through our nutrition program. - Before-and-after photos and stories to inspire and motivate new clients. 5. **Supplement Recommendations**: - Information on recommended supplements to support various health goals. - Guidelines on how to choose quality supplements and incorporate them into their diet. 6. **Seasonal Meal Plans**: - Sample meal plans that change with the seasons, highlighting seasonal produce and recipes. - Tips for adjusting nutrition habits to fit different times of the year. 7. **Printable Resources**: - Printable grocery shopping lists that align with the meal plans provided. - Meal prep schedules and templates that clients can print and use weekly. 8. **Client Community Section**: - Information about joining our client community, including social media groups or forums. - Opportunities for clients to share their own tips, recipes, and experiences. 9. **Additional Wellness Tips**: - Tips on other aspects of wellness, such as stress management techniques, sleep hygiene, and mindfulness practices. - Brief guides on integrating fitness routines with nutrition plans for holistic health improvement. 10. **Exclusive Discounts**: - Coupons or discounts for local health food stores, restaurants, or wellness products. - Special offers for additional services at Summit Vitality, like personal training sessions or wellness workshops. 11. **Professional Endorsements**: - Endorsements or tips from our in-house nutrition experts or external health professionals. - Quotes or advice from well-known figures in the fitness and nutrition industry. 12. **Sustainability Tips**: - Information on sustainable eating practices and how to reduce food waste. - Tips for choosing environmentally friendly and ethically sourced food options. Including these nice-to-haves can enhance the value and appeal of the Summit Vitality Nutrition Introductory Document, providing a more engaging and comprehensive resource for our clients.
Should not have
• Given that you are providing all of the content, here is an updated list of project must not haves: ### Project Must Not Haves (With Provided Content) 1. **Overly Technical Layout**: - Avoid complex layouts that make the document difficult to navigate. - Ensure the design supports easy reading and comprehension. 2. **Cluttered Design**: - Avoid overcrowding pages with too many images or design elements. - Maintain a clean and organized layout to enhance readability. 3. **Inconsistent Branding**: - Do not use colors, fonts, or design elements that deviate from Summit Vitality’s established branding guidelines. - Ensure all visuals align with our brand identity. 4. **Negative or Fear-Based Imagery**: - Avoid using images that convey negative emotions or fear. - Focus on positive, empowering visuals that inspire and encourage. 5. **Low-Quality Images**: - Do not use low-resolution or irrelevant images. - Ensure all visuals are high-quality and contribute meaningfully to the content. 6. **Distracting or Irrelevant Visuals**: - Avoid using images or design elements that distract from the core content. - Ensure all visual elements are relevant and enhance the message. 7. **Inconsistent Image Style**: - Avoid using images with varying styles and tones that don’t harmonize. - Ensure a consistent visual style throughout the document. 8. **Disorganized Structure**: - Do not present information in a haphazard or disjointed manner. - Ensure a logical flow and clear organization of content. 9. **Excessive White Space or Crowded Pages**: - Avoid pages that are either too sparse or too cluttered. - Balance white space and content to maintain visual appeal. 10. **Unprofessional Tone in Visuals**: - Avoid casual or unprofessional imagery. - Maintain a warm, friendly, and professional tone in all visual elements. 11. **Lack of Visual Hierarchy**: - Do not use designs that lack clear visual hierarchy. - Ensure that important information is highlighted and easily identifiable. 12. **Generic Stock Images**: - Avoid overusing generic stock images that do not add value to the content. - Use images that are specific and relevant to the content provided. This refined list ensures that the visual design complements the provided content effectively, enhancing readability and maintaining professional standards for the Summit Vitality Nutrition Introductory Document.

```html
<!DOCTYPE html>
<html lang="en">
<head>
<meta charset="utf-8">
<title>Summit Vitality – Nutrition Introductory Guide</title>
<link rel="stylesheet" href="https://fonts.googleapis.com/css2?family=Jura:wght@400;500;600&family=Orbitron:wght@500&display=swap">
<style>
  :root {
    --stage: #cfcfcf;
    --tan: #c49a6c;
    --tan-light: #caa274;
    --brown-deep: #5e3714;
    --brown-shadow: #4a2a12;
    --white: #ffffff;
    --photo-skin: #b98a5e;
    --photo-dark: #2a1c14;
    --photo-food: #9d8a52;
  }
  * { box-sizing: border-box; margin: 0; padding: 0; }
  html, body { width: 1200px; height: 2318px; overflow: hidden; }
  body {
    background: var(--stage);
    font-family: "Jura", sans-serif;
    color: var(--white);
    position: relative;
  }
  .page {
    position: absolute;
    left: 234px;
    width: 732px;
    height: 1034px;
    background: var(--tan);
    box-shadow: 6px 8px 10px rgba(0,0,0,.28);
    overflow: hidden;
  }
  .cover { top: 82px;
    background:
      radial-gradient(ellipse 260px 360px at 30px 500px, rgba(74,42,18,.85), rgba(74,42,18,0) 100%),
      linear-gradient(180deg, var(--tan) 0%, var(--tan-light) 100%);
  }
  .contents { top: 1200px;
    background:
      radial-gradient(ellipse 420px 260px at 366px 0, rgba(74,42,18,.9), rgba(74,42,18,0) 100%),
      var(--tan);
  }
  .band { position: absolute; }
  .band-dark { background: var(--brown-deep); }
  .band-light { background: var(--white); }
  .cover .band-top { left: 0; top: 51px; width: 406px; height: 45px; clip-path: polygon(0 0, 100% 0, 90% 100%, 0 100%); }
  .cover .band-accent { left: 491px; top: 925px; width: 178px; height: 19px; clip-path: polygon(9% 0, 100% 0, 91% 100%, 0 100%); }

  .photo { position: absolute; }
  .photo-athlete {
    left: 380px; top: 40px; width: 300px; height: 830px;
    background: radial-gradient(ellipse 50% 45% at 55% 35%, rgba(42,28,20,.55), rgba(185,138,94,0) 100%);
    border-radius: 40% 40% 20% 20%;
  }
  .photo-food {
    left: 50px; top: 760px; width: 682px; height: 274px;
    background: radial-gradient(ellipse 45% 60% at 65% 55%, rgba(157,138,82,.75), rgba(196,154,108,0) 100%);
  }

  .brand { position: absolute; left: 110px; top: 190px; display: flex; align-items: center; gap: 14px; }
  .brand-dot { width: 34px; height: 34px; border: 3px solid var(--white); border-radius: 50%; }
  .brand-name { font-weight: 600; font-size: 26px; letter-spacing: 2px; text-transform: uppercase; }

  .cover-title { position: absolute; left: 76px; top: 354px; line-height: 59px; font-weight: 500; font-size: 52px; letter-spacing: -1px; }
  .cover-title .line { display: block; }
  .cover-title .line-lead { font-size: 56px; }
  .cover-title .line-feature {
    font-family: "Orbitron", sans-serif; font-size: 84px; line-height: 104px;
    color: transparent; -webkit-text-stroke: 2px var(--white);
    transform: skewX(-14deg); transform-origin: left bottom; letter-spacing: 2px;
  }
  .cover-subtitle { position: absolute; left: 76px; top: 748px; font-size: 24px; line-height: 31px; font-weight: 500; }

  .toc-title { position: absolute; left: 0; right: 0; top: 134px; text-align: center; font-size: 54px; font-weight: 600; letter-spacing: -1px; }
  .toc-list { position: absolute; left: 81px; top: 282px; list-style: none; }
  .toc-item { height: 61.5px; display: flex; align-items: center; font-size: 23px; font-weight: 500; }
  .toc-tick { width: 50px; height: 44px; margin-right: 10px; }
  .toc-num { width: 92px; }
  .contents .band-bottom-dark { left: 57px; top: 959px; width: 288px; height: 29px; clip-path: polygon(11% 0, 100% 0, 92% 100%, 0 100%); }
  .contents .band-bottom-light { left: 276px; top: 963px; width: 179px; height: 18px; clip-path: polygon(7% 0, 100% 0, 93% 100%, 0 100%); }
</style>
</head>
<body>
  <section class="page cover">
    <div class="band band-dark band-top"></div>
    <div class="photo photo-athlete" role="img" aria-label="Photo of an athlete mid-jump in black training wear and coral running shoes"></div>
    <div class="photo photo-food" role="img" aria-label="Photo of a bowl of fresh fruit and vegetables beside a stethoscope"></div>
    <div class="brand"><span class="brand-dot"></span><span class="brand-name">Summit Vitality</span></div>
    <h1 class="cover-title">
      <span class="line line-lead">SUMMIT</span>
      <span class="line line-feature">VITALITY</span>
      <span class="line">NUTRITION</span>
      <span class="line">INTRODUCTORY</span>
      <span class="line">GUIDE</span>
    </h1>
    <p class="cover-subtitle">Your Comprehensive Guide<br>to Nutrition and Longevity</p>
    <div class="band band-light band-accent"></div>
  </section>

  <section class="page contents">
    <h2 class="toc-title">Table Of Contents</h2>
    <ol class="toc-list">
      <li class="toc-item"><svg class="toc-tick" viewBox="0 0 50 44"><polyline points="2,30 9,26 16,42 28,4 46,4" fill="none" stroke="#fff" stroke-width="2"/><polyline points="41,0 46,4 41,8" fill="none" stroke="#fff" stroke-width="2"/></svg><span class="toc-num">01</span><span>Our Beliefs</span></li>
      <li class="toc-item"><svg class="toc-tick" viewBox="0 0 50 44"><polyline points="2,30 9,26 16,42 28,4 46,4" fill="none" stroke="#fff" stroke-width="2"/><polyline points="41,0 46,4 41,8" fill="none" stroke="#fff" stroke-width="2"/></svg><span class="toc-num">02</span><span>What to Expect from Us</span></li>
      <li class="toc-item"><svg class="toc-tick" viewBox="0 0 50 44"><polyline points="2,30 9,26 16,42 28,4 46,4" fill="none" stroke="#fff" stroke-width="2"/><polyline points="41,0 46,4 41,8" fill="none" stroke="#fff" stroke-width="2"/></svg><span class="toc-num">03</span><span>Nutritional Guidelines</span></li>
      <li class="toc-item"><svg class="toc-tick" viewBox="0 0 50 44"><polyline points="2,30 9,26 16,42 28,4 46,4" fill="none" stroke="#fff" stroke-width="2"/><polyline points="41,0 46,4 41,8" fill="none" stroke="#fff" stroke-width="2"/></svg><span class="toc-num">04</span><span>Added Benefits</span></li>
      <li class="toc-item"><svg class="toc-tick" viewBox="0 0 50 44"><polyline points="2,30 9,26 16,42 28,4 46,4" fill="none" stroke="#fff" stroke-width="2"/><polyline points="41,0 46,4 41,8" fill="none" stroke="#fff" stroke-width="2"/></svg><span class="toc-num">05</span><span>Meet Our Team</span></li>
      <li class="toc-item"><svg class="toc-tick" viewBox="0 0 50 44"><polyline points="2,30 9,26 16,42 28,4 46,4" fill="none" stroke="#fff" stroke-width="2"/><polyline points="41,0 46,4 41,8" fill="none" stroke="#fff" stroke-width="2"/></svg><span class="toc-num">06</span><span>Wholesome Recipes</span></li>
      <li class="toc-item"><svg class="toc-tick" viewBox="0 0 50 44"><polyline points="2,30 9,26 16,42 28,4 46,4" fill="none" stroke="#fff" stroke-width="2"/><polyline points="41,0 46,4 41,8" fill="none" stroke="#fff" stroke-width="2"/></svg><span class="toc-num">07</span><span>Fitness Tracking Advice</span></li>
      <li class="toc-item"><svg class="toc-tick" viewBox="0 0 50 44"><polyline points="2,30 9,26 16,42 28,4 46,4" fill="none" stroke="#fff" stroke-width="2"/><polyline points="41,0 46,4 41,8" fill="none" stroke="#fff" stroke-width="2"/></svg><span class="toc-num">08</span><span>Your Commitment to Success</span></li>
      <li class="toc-item"><svg class="toc-tick" viewBox="0 0 50 44"><polyline points="2,30 9,26 16,42 28,4 46,4" fill="none" stroke="#fff" stroke-width="2"/><polyline points="41,0 46,4 41,8" fill="none" stroke="#fff" stroke-width="2"/></svg><span class="toc-num">09</span><span>Contact Details</span></li>
      <li class="toc-item"><svg class="toc-tick" viewBox="0 0 50 44"><polyline points="2,30 9,26 16,42 28,4 46,4" fill="none" stroke="#fff" stroke-width="2"/><polyline points="41,0 46,4 41,8" fill="none" stroke="#fff" stroke-width="2"/></svg><span class="toc-num">10</span><span>Pathway to Success</span></li>
    </ol>
    <div class="band band-dark band-bottom-dark"></div>
    <div class="band band-light band-bottom-light"></div>
  </section>
</body>
</html>
```